New website for Fribrix.se - self employment agency for freelance workers

[NOTE THE CODED ADD-ON HAS BEEN INCLUDED ALREADY (DC ADMIN)] New layout based on Wordpress themes including migration of existing content at fribrix.se. Want to use existing logotype as guideline for total layout concept. Please use existing structure and text content on fribrix.se. Existing pictures are optional to reuse. The secured part of the existing website under "Logga in" is not part of this project.

Target Market(s)

Self employment within all industries and ages above 16.

Industry/Entity Type

Finance And Accounting

Font styles to use
Other font styles liked:
• Should match with logotype

Colors
3176b5
85abd2
cfdeed

Requirements
Must have
• Ready to use wordpress themes. Include salary calculation bar as in existing website. Multi lingual ready(today only in Swedish). Mobile client responsive.

```html
<!DOCTYPE html>
<html lang="sv">
<head>
<meta charset="utf-8">
<title>Fribrix – Fakturera utan eget företag</title>
<link href="https://fonts.googleapis.com/css2?family=Montserrat:wght@400;500;600;700;800&family=Open+Sans:wght@400;600&display=swap" rel="stylesheet">
<style>
:root{
  --blue:#1170b8;
  --blue-mid:#85abd2;
  --blue-light:#cfdeed;
  --ink:#1b1b1b;
  --text:#555;
  --muted:#888;
  --gray-band:#ececec;
  --footer:#f3f3f3;
  --white:#fff;
  --green:#2aa54b;
}
*{box-sizing:border-box;margin:0;padding:0}
html,body{width:1200px;height:3243px;overflow:hidden}
body{font-family:"Open Sans",Arial,sans-serif;color:var(--text);background:var(--white);position:relative}
h1,h2,h3,h4,.nav,.btn,.logo{font-family:"Montserrat",Arial,sans-serif}
section,header,footer{position:absolute;left:0;width:1200px}
.abs{position:absolute}

/* header */
.site-header{top:0;height:65px;background:var(--white)}
.logo{display:flex;align-items:center;gap:8px;font-weight:500;font-size:19px;color:#2a3a4a;letter-spacing:1px}
.logo-dot{width:22px;height:22px;border-radius:50%;background:var(--blue)}
.site-header .logo{left:158px;top:20px}
.nav{left:520px;top:0;height:65px;display:flex;align-items:center;font-size:13.5px;font-weight:600;color:#222}
.nav a{color:inherit;text-decoration:none;padding:0 16px;height:65px;display:flex;align-items:center;position:relative}
.nav a.active::before{content:"";position:absolute;left:12px;right:12px;top:0;height:4px;background:var(--blue)}
.btn{display:inline-flex;align-items:center;justify-content:center;background:var(--blue);color:var(--white);font-weight:600;text-decoration:none;letter-spacing:.5px}
.nav .btn-sign{margin-left:24px;width:90px;height:32px;font-size:13px;padding:0}

/* hero */
.hero{top:65px;height:493px;background:linear-gradient(180deg,#8c8f93 0%,#6d7378 38%,#3f4750 62%,#5b5f63 80%,#3b3a38 100%)}
.hero h1{position:absolute;top:168px;width:100%;text-align:center;font-size:51px;font-weight:800;color:var(--white);letter-spacing:-.5px}
.hero .btn{position:absolute;left:540px;top:251px;width:120px;height:32px;font-size:11px}

/* intro */
.eyebrow{font-family:"Montserrat",sans-serif;font-size:16px;font-weight:700;color:#777;letter-spacing:2px;text-align:center}
.section-title{font-size:22px;font-weight:800;color:var(--ink);text-align:center}
.intro{top:558px;height:382px}
.intro .eyebrow{position:absolute;top:71px;width:100%}
.intro .section-title{position:absolute;top:98px;width:100%}
.feature-card{position:absolute;top:155px;width:430px;height:163px;background:var(--white);box-shadow:0 2px 14px rgba(0,0,0,.12);padding:32px 34px}
.feature-card h3{font-family:"Open Sans",sans-serif;font-size:14.5px;font-weight:600;color:var(--blue);line-height:19px;margin-bottom:14px}
.feature-card p{font-size:12px;line-height:21px;color:var(--muted)}

/* why */
.why{top:940px;height:424px;background:var(--gray-band)}
.why .section-title{position:absolute;top:78px;width:100%}
.why-card{position:absolute;top:132px;width:280px;height:217px;background:var(--white);box-shadow:0 2px 10px rgba(0,0,0,.08);text-align:center;padding-top:46px}
.why-card .why-icon{display:block;margin:0 auto;width:46px;height:46px}
.why-card ul{list-style:none;margin-top:20px;display:inline-block;text-align:left;font-size:12.5px;color:#333;line-height:24px}
.why-card li{display:flex;align-items:center;gap:9px;white-space:nowrap}
.why-card .tick{width:13px;height:10px;flex:none}

/* partner */
.partner{top:1364px;height:400px;background:radial-gradient(ellipse at 50% 50%,#3a3532 0%,#2b2826 45%,#1e1d1c 100%)}
.partner h2{position:absolute;top:78px;width:100%;text-align:center;color:var(--white);font-size:22px;font-weight:800}
.partner .body{position:absolute;top:126px;left:220px;width:760px;text-align:center;color:var(--white);font-size:12.5px;line-height:21px}
.partner .body p+p{margin-top:21px}

/* focus */
.focus{top:1764px;height:621px}
.focus .section-title{position:absolute;top:80px;width:100%}
.role{position:absolute;top:156px;width:280px;text-align:center}
.role .photo{width:280px;height:236px}
.role h4{margin-top:20px;font-size:15px;font-weight:700;color:#222;letter-spacing:1.5px}
.role p{margin-top:8px;font-size:12.5px;line-height:21px;color:var(--text)}
.arrow{position:absolute;top:290px;width:30px;height:20px}
.focus .btn{position:absolute;left:493px;top:512px;width:214px;height:35px;font-size:11.5px}

/* feed strip */
.feed{top:2385px;height:201px;display:flex}
.feed .tile{width:200px;height:201px}
.feed .follow{position:absolute;left:504px;top:71px;width:192px;height:56px;background:var(--white);font-family:"Montserrat",sans-serif;font-size:12.5px;font-weight:600;color:#222;display:flex;align-items:center;justify-content:center}

/* calculator */
.calc{top:2586px;height:393px}
.calc .section-title{position:absolute;top:83px;width:100%}
.calc-field{position:absolute;top:150px;width:230px;text-align:center}
.calc-field label{display:block;font-family:"Montserrat",sans-serif;font-size:12px;font-weight:700;color:#222;margin-bottom:10px;white-space:nowrap}
.calc-field .value{margin:0 auto;width:132px;height:35px;background:#efefef;color:var(--blue);font-family:"Montserrat",sans-serif;font-weight:600;font-size:12.5px;display:flex;align-items:center;justify-content:center}
.slider{position:absolute;left:309px;top:241px;width:582px;height:10px;border-radius:5px;background:#ececec}
.slider span{display:block;width:223px;height:10px;border-radius:5px;background:var(--blue)}
.age{position:absolute;top:292px;left:474px;display:flex;align-items:center;font-size:12px;color:#333}
.age strong{font-family:"Montserrat",sans-serif;font-weight:700;margin-right:28px;font-size:12px}
.radio{width:18px;height:18px;border-radius:50%;background:#e8e8e8;border:1px solid #ddd;margin-right:8px;position:relative}
.radio.on{background:var(--white);border:2px solid var(--blue)}
.radio.on::after{content:"";position:absolute;left:3px;top:3px;width:8px;height:8px;border-radius:50%;background:var(--blue)}
.age .opt{display:flex;align-items:center;margin-right:30px}

/* footer */
.site-footer{top:2979px;height:264px;background:var(--footer)}
.site-footer .logo{position:absolute;left:158px;top:46px}
.footer-about{position:absolute;left:158px;top:88px;width:240px;font-size:12px;line-height:21px;color:var(--muted)}
.footer-col{position:absolute;top:42px;font-size:11.5px;color:var(--muted);line-height:23px}
.footer-col h4{font-size:13px;font-weight:700;color:#222;margin-bottom:8px;letter-spacing:.5px}
.social{display:flex;align-items:center;gap:10px;margin-bottom:8px}
.social i{width:22px;height:22px;border-radius:50%;background:var(--blue);display:block}
.footer-rule{position:absolute;left:158px;top:211px;width:884px;height:1px;background:#ddd}
.footer-bottom{position:absolute;left:158px;top:230px;width:884px;display:flex;justify-content:space-between;font-size:11px;color:#444}
.footer-bottom .legal span+span::before{content:"|";margin:0 12px;color:#999}
</style>
</head>
<body>

<header class="site-header">
  <div class="logo abs"><span class="logo-dot"></span>FRIBRIX</div>
  <nav class="nav abs">
    <a class="active" href="#">HOME</a>
    <a href="#">SELF-EMPLOYED</a>
    <a href="#">BUSINESS</a>
    <a href="#">ABOUT US</a>
    <a class="btn btn-sign" href="#">SIGN N</a>
  </nav>
</header>

<section class="hero" role="img" aria-label="Misty mountain lake with a wooden pier and a person standing at the end">
  <h1>YOU CAN DO IT SOLO</h1>
  <a class="btn" href="#">GET STARTED</a>
</section>

<section class="intro">
  <p class="eyebrow">FAKTURERA UTAN EGET FÖRETAG</p>
  <h2 class="section-title">ANLITA MEDARBETARE UTAN ATT ANSTÄLLA</h2>
  <article class="feature-card" style="left:156px">
    <h3>Fokusera på att utföra uppdraget så tar vi hand om resten</h3>
    <p>Lorem ipsum dolor sit amet, consectetur adipisicing elit, sed do eiusmod tempor incididunt ut labore et dolore magna aliqua. Ut enim ad minim veniam, quis nostrud.</p>
  </article>
  <article class="feature-card" style="left:614px">
    <h3>Välj ut och anlita dina kompetenta medarbetare utan att anställa</h3>
    <p>Lorem ipsum dolor sit amet, consectetur adipisicing elit, sed do eiusmod tempor in cididunt ut labore et dolore magna aliqua. Ut enim ad minim veniam.</p>
  </article>
</section>

<section class="why">
  <h2 class="section-title">VARFÖR FRIBRIX?</h2>
  <svg width="0" height="0" style="position:absolute">
    <symbol id="tick" viewBox="0 0 14 11"><path d="M1 6l4 4L13 1" fill="none" stroke="#2aa54b" stroke-width="2.4"/></symbol>
  </svg>
  <div class="why-card" style="left:156px">
    <svg class="why-icon" viewBox="0 0 46 46" fill="none" stroke="#1170b8" stroke-width="2"><circle cx="22" cy="24" r="18"/><path d="M13 24l7 7 20-22"/></svg>
    <ul>
      <li><svg class="tick"><use href="#tick"/></svg>Beprövat lönesystem</li>
      <li><svg class="tick"><use href="#tick"/></svg>Erfarna medarbeterare</li>
      <li><svg class="tick"><use href="#tick"/></svg>Väletablerade kontakte</li>
    </ul>
  </div>
  <div class="why-card" style="left:460px">
    <svg class="why-icon" viewBox="0 0 46 46" fill="none" stroke="#1170b8" stroke-width="2"><path d="M17 8h12l-4 7h-4z"/><path d="M19 15c-8 5-12 12-10 19 1 5 6 7 14 7"/><path d="M27 15c5 3 8 7 9 11"/><ellipse cx="34" cy="32" rx="8" ry="3"/><path d="M26 32v6c0 2 4 3 8 3s8-1 8-3v-6"/></svg>
    <ul>
      <li><svg class="tick"><use href="#tick"/></svg>Endast 3,95 % avgift</li>
      <li><svg class="tick"><use href="#tick"/></svg>Kostnadsfritt konto</li>
      <li><svg class="tick"><use href="#tick"/></svg>Möjlighet till expressbetalning</li>
    </ul>
  </div>
  <div class="why-card" style="left:765px">
    <svg class="why-icon" viewBox="0 0 46 46" fill="none" stroke="#1170b8" stroke-width="2"><path d="M3 18l8-6 8 4 8-4 8 4 8-4"/><path d="M11 22l10 10c2 2 5 2 7 0l9-9"/><path d="M18 27l7 7M22 24l6 6"/><path d="M8 8l3 3M38 8l-3 3M23 4v4"/></svg>
    <ul>
      <li><svg class="tick"><use href="#tick"/></svg>Fakturera utan företag</li>
      <li><svg class="tick"><use href="#tick"/></svg>Enkla villkor</li>
      <li><svg class="tick"><use href="#tick"/></svg>Vi tar hand om all administration</li>
    </ul>
  </div>
</section>

<section class="partner" role="img" aria-label="Dark close-up of two people shaking hands across a table">
  <h2>FRIBRIX EN TRYGG PARTNER</h2>
  <div class="body">
    <p>Fribrix är ett egenanställningsföretag som ger människor möjlighet att nå sina drömmar och arbeta som egenföretagare utan eget företag. Vi frigör tid och skapar trygghet genom att ta hand om administrationen. Fribrix startade 2016 och ingår i Norvalo-koncernen. Norvalo har fått utmärkelser som Superföretag av Företagsveckan, Snabbväxare av Brandt &amp; Partners och Gasellföretag av Näringslivsbladet.</p>
    <p>Sedan 2008 har Norvalo dessutom en AAA-klassning från Kreditrating. Vi är helt enkelt en koncern med ordning på vår ekonomi. Norvalo grundades 2003 av Erik Lindqvist och Mats Berglund som är rutinerade entreprenörer med erfarenhet av konsultverksamhet sedan 1996. Erik är idag Norvalos koncernchef och Mats är styrelseordförande. http://www.norvalo.se/om-oss/</p>
  </div>
</section>

<section class="focus">
  <h2 class="section-title">FOKUSERA PÅ DET DU ÄR BRA PÅ!</h2>
  <svg class="arrow" style="left:84px" viewBox="0 0 30 20" fill="none" stroke="#333" stroke-width="2"><path d="M28 10H3M10 3L3 10l7 7"/></svg>
  <div class="role" style="left:156px">
    <div class="photo" role="img" aria-label="Two consultants in a meeting at a desk" style="background:linear-gradient(135deg,#b9a58c,#6f6a62 60%,#8b8a86)"></div>
    <h4>KONSULT</h4>
    <p>Lorem Ipsum is simply dummy text of the<br>printing and typesetting industry.</p>
  </div>
  <div class="role" style="left:460px">
    <div class="photo" role="img" aria-label="Artist's paint palette and brushes" style="background:linear-gradient(135deg,#d9cfc4,#c79a82 55%,#e8e2da)"></div>
    <h4>KONSTNER</h4>
    <p>Lorem Ipsum is simply dummy text of the<br>printing and typesetting industry.</p>
  </div>
  <div class="role" style="left:765px">
    <div class="photo" role="img" aria-label="Photographer holding a camera" style="background:linear-gradient(135deg,#c8c8c8,#4a4a4a 55%,#b06a6a)"></div>
    <h4>FOTOGRAF</h4>
    <p>Lorem Ipsum is simply dummy text of the<br>printing and typesetting industry.</p>
  </div>
  <svg class="arrow" style="left:1086px" viewBox="0 0 30 20" fill="none" stroke="#333" stroke-width="2"><path d="M2 10h25M20 3l7 7-7 7"/></svg>
  <a class="btn" href="#">VI HJÄLPER DIG MED RESTEN!</a>
</section>

<section class="feed">
  <div class="tile" role="img" aria-label="Handshake over a desk with laptop" style="background:linear-gradient(135deg,#6d6357,#a89e92)"></div>
  <div class="tile" role="img" aria-label="Calculator and documents on a desk" style="background:linear-gradient(135deg,#d8d4cf,#9a948c)"></div>
  <div class="tile" role="img" aria-label="Businessman in front of a brick wall" style="background:linear-gradient(135deg,#a0644a,#5b4a44)"></div>
  <div class="tile" role="img" aria-label="Thumbs up gesture" style="background:linear-gradient(135deg,#3a3a3a,#8f8a85)"></div>
  <div class="tile" role="img" aria-label="Glass skyscrapers from below" style="background:linear-gradient(135deg,#2f4e4f,#9fb3b1)"></div>
  <div class="tile" role="img" aria-label="Aerial view of people on a plaza" style="background:linear-gradient(135deg,#6b7a6a,#c2c9bf)"></div>
  <div class="follow">FOLLOW@PHOTOFEED</div>
</section>

<section class="calc">
  <h2 class="section-title">RÄKNA UT DIN LÖN!</h2>
  <div class="calc-field" style="left:350px"><label>FAKTURABELOPP EXKL. MOMS</label><div class="value">70500 SEK</div></div>
  <div class="calc-field" style="left:605px"><label>DIN NETTOLÖN</label><div class="value">36067 SEK</div></div>
  <div class="slider"><span></span></div>
  <div class="age">
    <strong>ÅLDER</strong>
    <div class="opt"><span class="radio"></span>Over 65</div>
    <div class="opt"><span class="radio on"></span>Under 65</div>
  </div>
</section>

<footer class="site-footer">
  <div class="logo"><span class="logo-dot"></span>FRIBRIX</div>
  <p class="footer-about">Duis bibendum nisi nec purus cursus facilisis. Fusce blandit lorem dolor non pellentesque velit venenatis bendm nisi purus cursus facilisis.</p>
  <div class="footer-col" style="left:473px">
    <h4>QUICK LINKS</h4>
    Home<br>Biography<br>Publications<br>The Group<br>Contact
  </div>
  <div class="footer-col" style="left:629px">
    <h4>CONTACT US</h4>
    1280 Elm Street Lakeview,<br>PA 15000<br>Phone: 555-010-2040<br>Email: info@studiolumen.com
  </div>
  <div class="footer-col" style="left:871px">
    <h4>FOLLOW US</h4>
    <div class="social"><i></i>WorkNet</div>
    <div class="social"><i></i>FaceSpace</div>
    <div class="social"><i></i>Chirper</div>
  </div>
  <div class="footer-rule"></div>
  <div class="footer-bottom">
    <span>Copyright © 2018 Fribrix - All Rights Reserved.</span>
    <span class="legal"><span>Terms &amp; conditions</span><span>Privacy policy</span></span>
  </div>
</footer>

</body>
</html>
```